Olive Oil label for bottle 0.5l approx. 10x12 cm

I am running a Spa hotel in Bavaria (logo attached) and my family lives in Greece (Bavarian and Greek flag have the same colors). They produce organic olive oil first cold pressed extra virgin. I would need a label for 0,5 liter bottles to reach them out to my guests and they should see the high quality of the olive oil and the family connection Spa-hotel Bavaria to family in Greece. The name of the family is Morvatek, the hotel is called Fernwald, the olive oil comes from Greece/Argolis/Kranidi. The name of the small olive company is Kerano Hawks. There should be a space for the best before date and the organic control number (handwritten) . The hotel logo is not mandatory. Should look nice 😉

```html
<!DOCTYPE html>
<html lang="en">
<head>
<meta charset="utf-8">
<title>Morvatek Olive Oil Label</title>
<link href="https://fonts.googleapis.com/css2?family=Jost:wght@400;500;600&display=swap" rel="stylesheet">
<style>
  :root {
    --backdrop: #ece6de;
    --label-green: #8b9a76;
    --cream: #f7e9de;
    --ink: #38382f;
    --sky-top: #4fb8ea;
    --sky-low: #cfe6f0;
    --village-white: #e9eef4;
    --alpine-sky: #f3e3b8;
    --alpine-rock: #8fa3b5;
    --meadow: #6f9a4a;
  }
  * { margin: 0; padding: 0; box-sizing: border-box; }
  html, body {
    width: 1200px; height: 897px; overflow: hidden;
    background: var(--backdrop);
  }
  .canvas { position: relative; width: 1200px; height: 897px; }
  .label {
    position: absolute; left: 450px; top: 0;
    width: 300px; height: 897px;
    background: var(--label-green);
    overflow: hidden;
    font-family: "Jost", sans-serif;
    color: var(--ink);
  }
  .scene { position: absolute; top: 0; height: 520px; }
  .scene--greek {
    left: 0; width: 150px;
    background: linear-gradient(180deg, var(--sky-top) 0%, var(--sky-low) 40%, var(--village-white) 62%, #c97f78 85%, #6b7fa0 100%);
  }
  .scene--alpine {
    left: 150px; width: 150px;
    background: linear-gradient(180deg, var(--alpine-sky) 0%, var(--alpine-rock) 30%, #a7b3bf 48%, var(--meadow) 70%, #5f8a3e 100%);
  }
  .emblem { position: absolute; left: 0; top: 0; }
  .ring-text { font-family: "Jost", sans-serif; font-weight: 500; fill: var(--ink); letter-spacing: 2px; }
  .ring-text--outer { font-size: 13.5px; }
  .ring-text--inner { font-size: 12px; letter-spacing: 1.5px; }
  .emblem-small { font-family: "Jost", sans-serif; font-weight: 500; font-size: 11px; letter-spacing: 1.5px; fill: var(--ink); }
  .brand-name { font-family: "Jost", sans-serif; font-weight: 500; font-size: 40px; fill: var(--ink); letter-spacing: 3px; }
  .fields {
    position: absolute; left: 29px; top: 770px;
    display: flex; gap: 16px;
  }
  .field { width: 113px; }
  .field__title {
    font-size: 7.5px; font-weight: 600; letter-spacing: 1.4px;
    color: var(--ink); text-align: center; margin-bottom: 6px;
  }
  .field__box { height: 19px; background: var(--cream); }
  .volume {
    position: absolute; left: 0; width: 100%; top: 818px;
    text-align: center; font-size: 14px; font-weight: 600;
    letter-spacing: 3.5px; color: var(--ink);
  }
  .hotel-name {
    position: absolute; left: 0; width: 100%; top: 856px;
    text-align: center; font-size: 15px; font-weight: 500;
    color: var(--cream);
  }
</style>
</head>
<body>
<div class="canvas">
  <div class="label">
    <div class="scene scene--greek" role="img" aria-label="Illustration of a whitewashed Greek chapel with blue domes above the sea"></div>
    <div class="scene scene--alpine" role="img" aria-label="Illustration of Bavarian alpine peaks above a village with a church tower and green meadows"></div>

    <svg class="emblem" width="300" height="897" viewBox="0 0 300 897">
      <defs>
        <path id="outer-top" d="M24 612 A122 122 0 0 1 268 612"/>
        <path id="outer-bottom" d="M10 612 A136 136 0 0 0 282 612"/>
        <path id="inner-top" d="M58 612 A88 88 0 0 1 234 612"/>
        <path id="inner-bottom" d="M48 612 A98 98 0 0 0 244 612"/>
      </defs>
      <path class="drop" fill="var(--cream)" d="M146 0 C150 230 290 430 290 612 A144 144 0 0 1 2 612 C2 430 142 230 146 0 Z"/>
      <circle cx="146" cy="612" r="104" fill="none" stroke="var(--ink)" stroke-width="1"/>
      <rect x="8" y="588" width="276" height="44" fill="var(--cream)"/>

      <text class="ring-text ring-text--outer"><textPath href="#outer-top" startOffset="50%" text-anchor="middle">KERANO HAWKS OLIVE OIL COMPANY</textPath></text>
      <text class="ring-text ring-text--outer"><textPath href="#outer-bottom" startOffset="50%" text-anchor="middle">GREECE - ARGOLIS - KRANIDI</textPath></text>
      <text class="ring-text ring-text--inner"><textPath href="#inner-top" startOffset="50%" text-anchor="middle">EXTRA VIRGIN</textPath></text>
      <text class="ring-text ring-text--inner"><textPath href="#inner-bottom" startOffset="50%" text-anchor="middle">OLIVE OIL</textPath></text>

      <text class="emblem-small" x="146" y="576" text-anchor="middle">ESTD</text>
      <text class="brand-name" x="146" y="625" text-anchor="middle">MORVATEK</text>
      <text class="emblem-small" x="146" y="656" text-anchor="middle">2023</text>
    </svg>

    <div class="fields">
      <div class="field">
        <div class="field__title">BEST BEFORE</div>
        <div class="field__box"></div>
      </div>
      <div class="field">
        <div class="field__title">ORGANIC CONTROL</div>
        <div class="field__box"></div>
      </div>
    </div>
    <div class="volume">500ML</div>
    <div class="hotel-name">Fernwald</div>
  </div>
</div>
</body>
</html>
```